Salon website

Need a web design for a new blow dry and hair extension boutique in CT
would like the color scheme to be gray, white and tiffany blue
Create a web site with about 4 pages showing
1 about us page
1 blow dry services page
1 hair extension services page
1 contact us page
1 membership page
1 parties page

Industry/Entity Type

Boutique

Colors
86cfc6
cfeae6
33b7a4
aaaaaa
cbcbcb
ffffff

```html
<!DOCTYPE html>
<html lang="en">
<head>
<meta charset="utf-8">
<title>Gloss &amp; Strand Boutique</title>
<link href="https://fonts.googleapis.com/css2?family=Open+Sans:ital,wght@0,400;0,600;1,400&display=swap" rel="stylesheet">
<style>
  :root {
    --tiffany: #12b9b5;
    --tiffany-text: #1ab3b0;
    --ink: #222222;
    --text: #444444;
    --muted: #888888;
    --rule: #a9aea6;
    --hero-bg: #cbdbca;
    --cream: #f8f4ed;
    --accent-red: #c0392b;
    --gold: #f1d58f;
    --footer: #222222;
    --footer-text: #b9b9b9;
    --white: #ffffff;
  }
  * { margin: 0; padding: 0; box-sizing: border-box; }
  html, body { width: 1062px; height: 1200px; overflow: hidden; }
  body { font-family: "Open Sans", sans-serif; color: var(--text); position: relative; background: var(--cream); }
  .abs { position: absolute; }

  .site-header { position: absolute; left: 0; top: 0; width: 1062px; height: 139px; background: var(--tiffany); }
  .brand { left: 88px; top: 16px; color: var(--white); font-size: 27px; line-height: 37px; font-weight: 600; text-transform: uppercase; letter-spacing: 0.5px; }
  .header-phone { right: 88px; top: 28px; color: var(--white); font-size: 20px; display: flex; align-items: center; gap: 8px; }
  .main-nav { right: 88px; top: 94px; display: flex; gap: 25px; font-size: 15px; color: var(--white); }
  .main-nav .current { color: var(--ink); }

  .hero { position: absolute; left: 0; top: 139px; width: 1062px; height: 408px; background: var(--hero-bg); }
  .hero-photo { left: 427px; top: 0; width: 635px; height: 408px; background: radial-gradient(ellipse at 55% 45%, #d9a35e 0%, #c98f4c 30%, #d7c4a0 55%, #cbdbca 78%); }
  .welcome-title { left: 91px; top: 79px; font-size: 31px; font-weight: 400; color: var(--ink); }
  .hero-rule { left: 88px; width: 364px; height: 1px; background: var(--rule); }
  .welcome-text { left: 100px; top: 143px; width: 345px; font-size: 13.5px; line-height: 22px; color: var(--text); }
  .book-btn { left: 88px; top: 281px; width: 170px; height: 39px; background: var(--ink); color: var(--gold); font-size: 14px; line-height: 39px; text-align: center; }
  .slider-dots { left: 487px; top: 366px; width: 90px; height: 19px; border-radius: 10px; background: rgba(60,60,60,0.75); display: flex; align-items: center; justify-content: center; gap: 9px; }
  .slider-dots span { width: 9px; height: 9px; border-radius: 50%; background: var(--white); }
  .slider-dots span.active { background: #555; border: 2px solid var(--white); }

  .testimonials-title { left: 0; width: 1062px; top: 583px; text-align: center; font-size: 24px; color: var(--ink); font-weight: 400; }
  .avatar { left: 112px; top: 629px; width: 111px; height: 111px; border-radius: 50%; border: 4px solid var(--white); box-shadow: 0 1px 4px rgba(0,0,0,0.25); background: radial-gradient(circle at 50% 45%, #8aa9b4, #4d6f7b); }
  .quote { left: 241px; top: 629px; width: 712px; font-size: 13px; line-height: 22px; font-style: italic; color: var(--muted); }
  .client-name { left: 241px; top: 708px; font-size: 13.5px; color: var(--tiffany-text); }
  .arrow { top: 668px; }
  .section-rule { left: 88px; top: 767px; width: 886px; height: 1px; background: #cfcac1; }

  .contact-line { left: 0; width: 1062px; display: flex; justify-content: center; align-items: center; gap: 8px; font-size: 13.5px; color: var(--text); }
  .address { top: 801px; color: var(--accent-red); font-size: 15px; }
  .calls { top: 836px; }
  .hours { top: 865px; }
  .sep { margin: 0 8px; }

  .map { left: 0; top: 926px; width: 1062px; height: 162px; background: linear-gradient(180deg, #dedede, #d3d3d3); }

  .site-footer { position: absolute; left: 0; top: 1088px; width: 1062px; height: 112px; background: var(--footer); }
  .footer-nav { left: 88px; top: 30px; font-size: 12.5px; color: var(--footer-text); }
  .footer-nav .sep { color: #666; }
  .copyright { left: 88px; top: 64px; font-size: 12.5px; color: var(--footer-text); }
  .social { top: 43px; width: 28px; height: 28px; border-radius: 50%; }
  .social-a { left: 905px; background: #3b5998; }
  .social-b { left: 946px; background: #2aa9e0; }
</style>
</head>
<body>
  <header class="site-header">
    <div class="abs brand">Gloss &amp;<br>Strand<br>Boutique</div>
    <div class="abs header-phone">
      <svg width="20" height="18" viewBox="0 0 20 18" aria-hidden="true"><path d="M4 1 L7 1 L8 5 L6 7 Q8 11 12 12 L14 10 L18 11 L18 14 Q17 17 13 16 Q4 13 2 4 Q2 1 4 1 Z" fill="#fff"/></svg>
      <span>555 014 2297</span>
    </div>
    <nav class="abs main-nav">
      <span class="current">Home</span><span>About us</span><span>Blow Dry</span><span>Hair Extensions services</span><span>Contact us</span>
    </nav>
  </header>

  <section class="hero">
    <div class="abs hero-photo" role="img" aria-label="Portrait of a woman with long voluminous curled blonde hair"></div>
    <h1 class="abs welcome-title">Welcome!</h1>
    <div class="abs hero-rule" style="top:126px"></div>
    <p class="abs welcome-text">Maecenas ipsum arcu, bibendum nec ultrices nec, gravida vel mauris. Curabitur dignissim lectus cursus est volutpat, eu laoreet nibh porta. Maecenas ipsum metus, accumsan a sapien eu, sodales tincidunt metus. Mauris gravida mi ac purus cursus suscipit.</p>
    <div class="abs hero-rule" style="top:266px"></div>
    <div class="abs book-btn">Book an Appointment</div>
    <div class="abs slider-dots"><span class="active"></span><span></span><span></span><span></span></div>
  </section>

  <h2 class="abs testimonials-title">Clients Testimonials</h2>
  <svg class="abs arrow" style="left:36px" width="16" height="32" viewBox="0 0 16 32" aria-hidden="true"><path d="M14 2 L2 16 L14 30" fill="none" stroke="#aaa" stroke-width="2"/></svg>
  <div class="abs avatar" role="img" aria-label="Client portrait photo"></div>
  <p class="abs quote">“ Nam a malesuada libero. Duis sodales et libero vel interdum. Interdum et malesuada fames ac ante ipsum primis in faucibus. Donec lobortis dui tortor, eu lobortis felis mattis nec. Sed justo quam, luctus eu mauris eget, euismod dapibus sem. Sed tempus feugiat ante, at ornare libero volutpat sed. Maecenas quis magna magna. ”</p>
  <div class="abs client-name">Marisa</div>
  <svg class="abs arrow" style="left:1009px" width="16" height="32" viewBox="0 0 16 32" aria-hidden="true"><path d="M2 2 L14 16 L2 30" fill="none" stroke="#aaa" stroke-width="2"/></svg>
  <div class="abs section-rule"></div>

  <div class="abs contact-line address">
    <svg width="12" height="18" viewBox="0 0 12 18" aria-hidden="true"><path d="M6 1 A5 5 0 0 1 11 6 Q11 10 6 17 Q1 10 1 6 A5 5 0 0 1 6 1 Z" fill="#c0392b"/><circle cx="6" cy="6" r="2" fill="#f8f4ed"/></svg>
    <span>55, Building name, Street name, City - Zip code</span>
  </div>
  <div class="abs contact-line calls">
    <svg width="18" height="12" viewBox="0 0 18 12" aria-hidden="true"><rect x="0.5" y="0.5" width="17" height="11" fill="#777"/><path d="M0.5 0.5 L9 7 L17.5 0.5" fill="none" stroke="#f8f4ed" stroke-width="1.2"/></svg>
    <span>Call : 555 014 2297<span class="sep">/</span>E-mail : hello@glossandstrand.com</span>
  </div>
  <div class="abs contact-line hours">
    <svg width="18" height="18" viewBox="0 0 18 18" aria-hidden="true"><circle cx="9" cy="9" r="7.5" fill="none" stroke="#777" stroke-width="1.5"/><path d="M9 4 V9 L12 11" fill="none" stroke="#777" stroke-width="1.5"/></svg>
    <span>Mon - Fre › 9:00 am to 6.00 pm<span class="sep">/</span>Sat › 9:00 am to 2.00 pm<span class="sep">/</span>Sunday Holiday</span>
  </div>

  <div class="abs map" role="img" aria-label="Street map showing the boutique location"></div>

  <footer class="site-footer">
    <div class="abs footer-nav">Home <span class="sep">/</span> About us <span class="sep">/</span> Blow Dry <span class="sep">/</span> Hair Extensions services <span class="sep">/</span> Contact us</div>
    <div class="abs copyright">Copyright ©&nbsp; 2014 &nbsp; Gloss &amp; Strand Boutique. &nbsp;All rights reserved.</div>
    <div class="abs social social-a" aria-label="Social profile"></div>
    <div class="abs social social-b" aria-label="Social profile"></div>
  </footer>
</body>
</html>
```